K-12 Education site

We are looking for a Wordpress theme that does the following:
- Uses our school colors: green and gold/yellow (not a true requirement as these colors can be pretty ugly)
- Works on all mobile devices and scales properly
- We are an Arts and Technology school so we would like the design to be clean, vibrant, and yet make use of HTML5
- Unique design

Target Market(s)

Prospective students and current students

Industry/Entity Type

School

Requirements
Must have
• Clean and unique Design
HTML5
Must scale for mobile devices

```html
<!DOCTYPE html>
<html lang="en">
<head>
<meta charset="utf-8">
<title>Riverbend Regional Governor's School</title>
<link rel="stylesheet" href="https://fonts.googleapis.com/css2?family=PT+Sans:wght@400;700&display=swap">
<style>
:root{
  --green:#1f5c40;
  --green-dark:#174a33;
  --green-text:#1d5a3c;
  --gold:#f2b21e;
  --gold-text:#f4b63a;
  --ink:#222;
  --body:#4a4a4a;
  --muted:#8a8a8a;
  --line:#d8d8d8;
  --footer:#2e2e2e;
  --doc:#8a8a8a;
}
*{box-sizing:border-box;margin:0;padding:0}
html,body{width:1200px;height:1148px;overflow:hidden}
body{font-family:"PT Sans",sans-serif;color:var(--body);background:#fff}
a{color:inherit;text-decoration:none}
.stage{width:1150px;height:1100px;transform:scale(1.04348);transform-origin:0 0;position:relative;
  background:linear-gradient(#e4e4e4 345px,#fafafa 900px,#fff 1003px)}
.top-band{position:absolute;left:0;top:0;width:1150px;height:345px;background:linear-gradient(#1e5c40,#205e43)}
.main-nav{position:absolute;left:91px;top:11px;display:flex;font-size:15px;color:#fff}
.main-nav a{height:28px;line-height:28px;padding:0 13px;margin-right:11px;border-radius:3px}
.main-nav a.active{background:var(--gold);color:#3a2a00;border:1px solid #d99a10;margin-right:17px}
.panel{position:absolute;left:86px;top:53px;width:978px;height:950px;background:#fff}
.brand{position:absolute;left:96px;top:70px;width:266px;height:262px;display:flex;flex-direction:column;align-items:center;justify-content:center;gap:14px;text-align:center}
.brand-mark{width:70px;height:70px;border-radius:50%;background:var(--gold)}
.brand-name{font-weight:700;font-size:22px;line-height:1.2;color:var(--green-text)}
.brand-place{font-weight:700;font-size:13px;letter-spacing:1px;color:var(--green-text)}
.slider{position:absolute;left:379px;top:70px;width:672px;height:275px;border:3px solid #cfcfcf;background:#ccc}
.slider .photo{position:absolute;inset:0;background:linear-gradient(160deg,#8a7a66,#3e5a48 55%,#b69c78)}
.slider .caption{position:absolute;left:0;right:0;bottom:0;height:50px;background:rgba(20,20,20,.7);color:#fff;font-size:18px;font-weight:700;line-height:50px;padding-left:20px}
.slider .arrows{position:absolute;right:16px;bottom:12px;display:flex;gap:3px}
.slider .arrows span{width:25px;height:25px;border-radius:50%;background:#eee;border:1px solid #999;display:flex;align-items:center;justify-content:center}
.search{position:absolute;left:95px;top:370px;width:265px;height:49px;background:#333;border-radius:3px;padding:5px}
.search .field{background:#fff;height:39px;border-radius:2px;display:flex;align-items:center;padding:0 6px 0 20px;justify-content:space-between;font-size:14px;color:#777}
.search .btn{width:24px;height:22px;background:#888;border-radius:2px;display:flex;align-items:center;justify-content:center}
.news{position:absolute;left:95px;top:430px;width:265px;height:370px;background:var(--green);border:1px solid var(--green-dark);border-radius:3px;padding:0 5px}
.news h2{color:var(--gold-text);font-size:21px;font-weight:700;height:40px;line-height:46px;padding-left:12px;position:relative}
.news h2 .more{position:absolute;right:10px;top:15px;width:17px;height:16px;background:#eee;border-radius:2px;display:flex;align-items:center;justify-content:center}
.news-item{background:#fff;height:76px;margin-bottom:5px;padding:6px 6px 0 27px;position:relative;font-size:13.5px;line-height:20px;color:#333}
.news-item::before{content:"";position:absolute;left:15px;top:13px;width:5px;height:5px;border-right:1.5px solid #444;border-top:1.5px solid #444;transform:rotate(45deg)}
.news-item time{display:block;font-size:12px;color:var(--muted);margin-top:2px}
.news-item:first-of-type{margin-top:6px}
.welcome h1{position:absolute;left:381px;top:368px;font-size:22px;font-weight:700;color:var(--green-text)}
.welcome p{position:absolute;left:381px;top:410px;width:418px;font-size:13.2px;letter-spacing:-0.25px;line-height:24px;text-align:justify}
.welcome .building{position:absolute;left:821px;top:413px;width:233px;height:128px;border:3px solid #cfcfcf;border-radius:3px;background:linear-gradient(#dfe8f0,#a88a62 55%,#2f4a2c)}
.divider{position:absolute;left:380px;top:578px;width:675px;height:1px;background:var(--line)}
.services h2{position:absolute;left:381px;top:597px;font-size:22px;font-weight:700;color:var(--green-text)}
.service{position:absolute;top:642px;width:162px;text-align:center}
.service .thumb{height:124px;border:1px solid #ccc}
.service span{display:block;margin-top:12px;font-size:15px;font-weight:700;color:#333}
.notice{position:absolute;left:95px;top:817px;width:960px;height:119px;background:#eee;border:1px solid #d6d6d6;border-radius:3px;padding:20px 24px;color:#222}
.notice strong{display:block;font-size:17px;line-height:24px}
.notice p{font-size:14.5px;margin-top:6px}
.downloads{position:absolute;left:95px;top:955px;width:960px;display:flex;justify-content:space-between}
.downloads a{display:flex;align-items:center;gap:10px;font-size:16px;font-weight:700;color:var(--green-text)}
.site-footer{position:absolute;left:0;top:1003px;width:1150px;height:97px;background:linear-gradient(#3a3a3a,#222)}
.footer-nav{position:absolute;left:86px;top:20px;font-size:14px;color:#bbb}
.footer-nav a+a::before{content:"|";margin:0 10px;color:#888}
.copyright{position:absolute;left:86px;top:54px;font-size:14px;color:#bbb}
.social{position:absolute;right:84px;top:35px;display:flex;gap:14px}
.social span{width:28px;height:28px;background:#e6e6e6;border-radius:2px}
</style>
</head>
<body>
<div class="stage">
  <div class="top-band"></div>
  <nav class="main-nav">
    <a class="active" href="#">Home</a><a href="#">Discover RRGS</a><a href="#">Students/Parents</a><a href="#">Faculty/Staff</a><a href="#">Doucments/Forms</a><a href="#">Programs of Study</a><a href="#">Services</a><a href="#">Contact us</a>
  </nav>
  <div class="panel"></div>

  <div class="brand">
    <span class="brand-mark"></span>
    <span class="brand-name">Riverbend Regional<br>Governor's School</span>
    <span class="brand-place">MILLBROOK, VA</span>
  </div>

  <section class="slider">
    <div class="photo" role="img" aria-label="Group of cheerleaders in green uniforms posing in the school gym"></div>
    <div class="caption">Located in Historic Downtown Millbrook</div>
    <div class="arrows">
      <span><svg width="10" height="10" viewBox="0 0 10 10"><path d="M7 1L3 5l4 4" fill="none" stroke="#333" stroke-width="2"/></svg></span>
      <span><svg width="10" height="10" viewBox="0 0 10 10"><path d="M3 1l4 4-4 4" fill="none" stroke="#333" stroke-width="2"/></svg></span>
    </div>
  </section>

  <form class="search">
    <div class="field">Search
      <span class="btn"><svg width="12" height="12" viewBox="0 0 12 12"><circle cx="5" cy="5" r="3.5" fill="none" stroke="#fff" stroke-width="1.6"/><path d="M7.5 7.5L11 11" stroke="#fff" stroke-width="1.8"/></svg></span>
    </div>
  </form>

  <aside class="news">
    <h2>Latest News <span class="more"><svg width="8" height="8" viewBox="0 0 8 8"><path d="M2 1l3 3-3 3" fill="none" stroke="#333" stroke-width="1.6"/></svg></span></h2>
    <div class="news-item">Pellentesque fringilla tristique ipsum, at sodales risus tincidunt tempor.<time>August-7-13</time></div>
    <div class="news-item">Pellentesque fringilla tristique ipsum, at sodales risus tincidunt tempor.<time>August-7-13</time></div>
    <div class="news-item">Pellentesque fringilla tristique ipsum, at sodales risus tincidunt tempor.<time>August-7-13</time></div>
    <div class="news-item">Pellentesque fringilla tristique ipsum, at sodales risus tincidunt tempor.<time>August-7-13</time></div>
  </aside>

  <section class="welcome">
    <h1>Welcome to Riverbend Regional Governor's School</h1>
    <p>Pellentesque tincidunt erat eget est suscipit ornare. In non ultricies mi. In id venenatis odio, ac hendrerit nisi. Interdum et malesuada fames ac ante ipsum primis in faucibus. Vivamus in porttitor nisi. Sed porta nisi vitae sem viverra porttitor. Fusce eget ligula eu elit convallis placerat. Cras euismod rutrum varius. Aenean dapibus diam ultricies odio.Etiam nec augue arcu. Integer in viverra orci, eu ullamcorper libero.</p>
    <div class="building" role="img" aria-label="Historic brick school building with rounded facade among trees"></div>
  </section>

  <div class="divider"></div>

  <section class="services">
    <h2>Our Services</h2>
    <div class="service" style="left:380px"><div class="thumb" role="img" aria-label="Student working at a computer" style="background:linear-gradient(135deg,#f2f2f2,#c9b59e 60%,#6b4a34)"></div><span>Information Technology</span></div>
    <div class="service" style="left:551px"><div class="thumb" role="img" aria-label="Students reading in the library stacks" style="background:linear-gradient(135deg,#7d8a96,#c9a276 60%,#5a4a3c)"></div><span>Library</span></div>
    <div class="service" style="left:722px"><div class="thumb" role="img" aria-label="Students eating lunch together in the cafe" style="background:linear-gradient(135deg,#6a4a34,#d9a57e 55%,#a5683c)"></div><span>Lunch/Cafe</span></div>
    <div class="service" style="left:893px"><div class="thumb" role="img" aria-label="Counselor talking with a student at a desk" style="background:linear-gradient(135deg,#eef0f2,#c7b298 55%,#5c5a5e)"></div><span>School Counseling</span></div>
  </section>

  <section class="notice">
    <strong>SUMMER HOURS: Offices are open 8AM to 4PM Monday through Thursday and closed from noon to 1PM for lunch. RRGS is closed on Fridays.</strong>
    <p>All building doors remain secure through the summer therefore all visitors please enter through the courtyard and press the buzzer for assistance.</p>
  </section>

  <div class="downloads">
    <a href="#"><svg width="24" height="25" viewBox="0 0 24 25"><path d="M4 1h11l5 5v18H4z" fill="#fff" stroke="var(--doc)" stroke-width="1.5"/><path d="M15 1v5h5M8 12h8M8 16h8M8 20h5" fill="none" stroke="var(--doc)" stroke-width="1.5"/></svg>2013-2014 Student Handbook</a>
    <a href="#"><svg width="24" height="25" viewBox="0 0 24 25"><path d="M4 1h11l5 5v18H4z" fill="#fff" stroke="var(--doc)" stroke-width="1.5"/><path d="M15 1v5h5M8 12h8M8 16h8M8 20h5" fill="none" stroke="var(--doc)" stroke-width="1.5"/></svg>English Department Summer Reading 2013</a>
    <a href="#"><svg width="24" height="25" viewBox="0 0 24 25"><path d="M4 1h11l5 5v18H4z" fill="#fff" stroke="var(--doc)" stroke-width="1.5"/><path d="M15 1v5h5M8 12h8M8 16h8M8 20h5" fill="none" stroke="var(--doc)" stroke-width="1.5"/></svg>Literary Arts Summer Reading 2013</a>
  </div>

  <footer class="site-footer">
    <nav class="footer-nav"><a href="#">Home</a><a href="#">Discover RRGS</a><a href="#">Students/Parents</a><a href="#">Faculty/Staff</a><a href="#">Doucments/Forms</a><a href="#">Programs of Study</a><a href="#">Services</a><a href="#">Contact us</a></nav>
    <p class="copyright">Copyright &copy; &nbsp;2013 &nbsp;RRGS. &nbsp;&nbsp;All rights reserved.</p>
    <div class="social"><span></span><span></span><span></span></div>
  </footer>
</div>
</body>
</html>
```